German tourism publishing house needs for international wellness hotel guide

We are planning as a print catalog. For this hotel directory we need a meaningful and appealing cover. The contents, a wide offer of wellness hotels should be recognizable at first sight. The title should make you want to go on a wellness holiday. The target group of the book are customers. We are looking forward to your next visit! The title "Wellness Hotels" should be larger on the cover written. The "Ravendo logo" should be smaller on the cover. Please integrate the Internet address www.ravendo-reisen.de small on the cover

Industry/Entity Type

Tourism

Font styles to use
Serif
Sans Serif

Colors
0355a3
ffffff
85acd3

Requirements
Must have
• We are looking forward to your next visit! The title "Wellness Hotels" should be larger on the cover written. The "Ravendo logo" should be smaller on the cover.
Nice to have
• Please integrate the Internet address www.ravendo-reisen.de small on the cover

```html
<!DOCTYPE html>
<html lang="de">
<head>
<meta charset="utf-8">
<title>Ravendo – Wellness Hotels</title>
<link rel="stylesheet" href="https://fonts.googleapis.com/css2?family=Marcellus+SC&family=Marcellus&family=Open+Sans:wght@600&display=swap">
<style>
  :root {
    --page-bg: #ececec;
    --cover-top: #1d3a73;
    --cover-mid: #0355a3;
    --cover-low: #2f6cc0;
    --accent-light: #85acd3;
    --white: #ffffff;
    --band-line: #0a3f8c;
  }
  html, body {
    margin: 0;
    width: 1200px;
    height: 800px;
    overflow: hidden;
    background: var(--page-bg);
  }
  .canvas {
    position: relative;
    width: 1200px;
    height: 800px;
  }
  .cover {
    position: absolute;
    left: 340px;
    top: 30px;
    width: 520px;
    height: 740px;
    overflow: hidden;
    background: linear-gradient(180deg, var(--cover-top) 0%, #1f4a92 30%, var(--cover-mid) 55%, var(--cover-low) 75%);
    box-shadow: 0 10px 30px rgba(0,0,0,0.18);
  }
  .cover-art {
    position: absolute;
    inset: 0;
  }
  .brand {
    position: absolute;
    top: 48px;
    left: 0;
    width: 100%;
    text-align: center;
    font-family: "Marcellus", serif;
    font-size: 26px;
    color: var(--white);
    letter-spacing: 0.5px;
  }
  .brand-dot {
    display: inline-block;
    width: 7px;
    height: 7px;
    border-radius: 50%;
    background: var(--white);
    margin-left: 4px;
    vertical-align: 14px;
  }
  .title {
    position: absolute;
    margin: 0;
    font-family: "Marcellus SC", serif;
    font-weight: 400;
    color: var(--white);
    line-height: 1;
    letter-spacing: 7px;
    font-size: 72px;
    white-space: nowrap;
  }
  .title-first {
    top: 92px;
    left: 36px;
  }
  .title-second {
    top: 170px;
    left: 168px;
  }
  .url-band {
    position: absolute;
    left: 0;
    bottom: 0;
    width: 100%;
    height: 58px;
    background: var(--white);
    border-top: 8px solid var(--band-line);
    box-sizing: border-box;
  }
  .url-band::after {
    content: "";
    position: absolute;
    left: 0;
    bottom: 0;
    width: 100%;
    height: 12px;
    background: var(--band-line);
  }
  .url {
    position: absolute;
    top: 12px;
    width: 100%;
    text-align: center;
    font-family: "Open Sans", sans-serif;
    font-weight: 600;
    font-size: 13px;
    letter-spacing: 2.5px;
    color: var(--band-line);
  }
</style>
</head>
<body>
<div class="canvas">
  <div class="cover">
    <svg class="cover-art" width="520" height="740" viewBox="0 0 520 740" xmlns="http://www.w3.org/2000/svg">
      <defs>
        <linearGradient id="street-fade" x1="0" y1="0" x2="0" y2="1">
          <stop offset="0" stop-color="#2f6cc0" stop-opacity="0"/>
          <stop offset="0.22" stop-color="#4a4a4e" stop-opacity="0.85"/>
          <stop offset="0.5" stop-color="#2e2b2a"/>
          <stop offset="0.72" stop-color="#6b6560"/>
          <stop offset="1" stop-color="#8f8a84"/>
        </linearGradient>
        <radialGradient id="street-warmth" cx="0.55" cy="0.45" r="0.45">
          <stop offset="0" stop-color="#b0483a" stop-opacity="0.55"/>
          <stop offset="0.6" stop-color="#6a3a2c" stop-opacity="0.25"/>
          <stop offset="1" stop-color="#3a3a3c" stop-opacity="0"/>
        </radialGradient>
        <radialGradient id="sauna-tones" cx="0.4" cy="0.35" r="0.8">
          <stop offset="0" stop-color="#ffe2c0"/>
          <stop offset="0.35" stop-color="#e39a5c"/>
          <stop offset="0.75" stop-color="#a85a30"/>
          <stop offset="1" stop-color="#8a6a9a"/>
        </radialGradient>
        <linearGradient id="pool-tones" x1="0" y1="0" x2="0" y2="1">
          <stop offset="0" stop-color="#a8642a"/>
          <stop offset="0.3" stop-color="#e8b070"/>
          <stop offset="0.55" stop-color="#f6dfa8"/>
          <stop offset="0.75" stop-color="#8fd3dc"/>
          <stop offset="1" stop-color="#b07048"/>
        </linearGradient>
        <radialGradient id="spa-tones" cx="0.5" cy="0.45" r="0.7">
          <stop offset="0" stop-color="#f0d8b8"/>
          <stop offset="0.4" stop-color="#e3964a"/>
          <stop offset="0.8" stop-color="#9a5228"/>
          <stop offset="1" stop-color="#5a3320"/>
        </radialGradient>
      </defs>

      <g role="img" aria-label="Photo of a half-timbered hotel with flower boxes on a cobbled village street under a blue sky">
        <rect x="0" y="400" width="520" height="282" fill="url(#street-fade)"/>
        <rect x="0" y="400" width="520" height="282" fill="url(#street-warmth)"/>
      </g>

      <g stroke="var(--white)" stroke-width="5">
        <path role="img" aria-label="Photo of a wood-panelled sauna with warm lighting"
              d="M16 345 C28 272 120 238 226 240 C200 300 150 356 84 358 C48 359 22 355 16 345 Z"
              fill="url(#sauna-tones)"/>
        <path role="img" aria-label="Photo of an indoor pool under a wooden ceiling"
              d="M20 478 C32 405 124 371 230 373 C204 433 154 489 88 491 C52 492 26 488 20 478 Z"
              fill="url(#pool-tones)"/>
        <path role="img" aria-label="Photo of a spa area with a salt wall and sauna door"
              d="M26 608 C38 535 130 501 236 503 C210 563 160 619 94 621 C58 622 32 618 26 608 Z"
              fill="url(#spa-tones)"/>
      </g>
    </svg>

    <div class="brand">Ravendo<span class="brand-dot"></span></div>
    <h1 class="title title-first">Wellness</h1>
    <h1 class="title title-second">Hotels</h1>

    <div class="url-band">
      <div class="url">www.ravendo-reisen.de</div>
    </div>
  </div>
</div>
</body>
</html>
```